Private practice for psychiatry and psychotherapy needs a business card and logo

I need a logo and business card design for my private practice for psychiatry and psychotherapy. The optional names for my practice are: Vornhoute Praktijk voor Psychiatrie en Psychotherapie, or short: Praktijk Vornhoute.
I am a (child and adolescent) psychiatrist and psychotherapist. I diagnose and treat infants, children, adolescents and adults with psychiatric symptoms/disorders. I also give supervision to colleagues about their own treatments. My work is characterised by personal involvement, transparence, creativity and professionality.
I would like to have an appealing, light and bright, yet basic design that invites people (both children and adults) to contact me, gives trust and hope, without loosing professional appearance.
I uploaded my contact information which should not necessarily be all included (in this form) on the card as long as people know how to contact me. Please feel free to be creative!
Please note that my website is only temporarely and need a new design and update too!

Target Market(s)

Clients and patients (children, adolescents, adults) with psychiatric symptoms who need diagnosis and treatment. I work with private clients and patients through medical insurances.

Industry/Entity Type

Mental Health

Contact Information for Business Card

Dr. Sanne Vornhoute-ter Kuilen
Psychiater/Kinder- en Jeugdpsychiater
Wouter Heskampstraat 14
3071 PX Rotterdam
t: 06-51928764
e: info@praktijkvornhoute.nl
i: www.praktijkvornhoute.nl

Logo Text

Praktijk Vornhoute voor Psychiatrie en Psychotherapie; or short: Praktijk Vornhoute

Font styles to use
Sans Serif
Other font styles liked:
• up to designer

Requirements
Must have
• Appealing, light, bright, creative, trustful, professional and unique.

```html
<!DOCTYPE html>
<html lang="nl">
<head>
<meta charset="utf-8">
<title>Praktijk Vornhoute – Visitekaartje</title>
<link rel="stylesheet" href="https://fonts.googleapis.com/css2?family=Montserrat:wght@700&family=Open+Sans:wght@400&family=Roboto+Condensed:wght@700&display=swap">
<style>
  :root {
    --page-bg: #e9ecef;
    --card-white: #ffffff;
    --card-shade: #eeeeee;
    --ink-dark: #4a4a4a;
    --ink-grey: #6b6b6b;
    --rule-grey: #8a8a8a;
    --brand-blue: #2a8fd0;
    --brand-blue-light: #3aa6dc;
    --brand-blue-deep: #17508a;
    --mark-silver: #b9bec4;
  }
  * { box-sizing: border-box; margin: 0; padding: 0; }
  html, body {
    width: 1200px; height: 1000px; overflow: hidden;
    background: var(--page-bg);
  }
  .canvas {
    position: relative; width: 1200px; height: 1000px;
  }
  .card {
    position: absolute; left: 250px; width: 700px; height: 400px;
    border-radius: 22px; overflow: hidden;
    box-shadow: 0 10px 30px rgba(0,0,0,.18);
  }
  .card--front {
    top: 60px;
    background: linear-gradient(160deg, var(--card-white) 55%, var(--card-shade) 100%);
  }
  .card--back {
    top: 540px;
    background: radial-gradient(ellipse at 55% 40%, var(--brand-blue-light) 0%, var(--brand-blue) 45%, var(--brand-blue-deep) 100%);
    display: flex; align-items: center; justify-content: center;
  }
  .practice-name {
    display: flex; align-items: center; gap: 10px;
    font-family: "Montserrat", sans-serif; font-weight: 700;
    text-transform: uppercase; letter-spacing: .5px;
  }
  .practice-name__dot { width: 14px; height: 14px; border-radius: 50%; }
  .card--front .practice-name {
    position: absolute; right: 48px; top: 96px;
    font-size: 17px; color: var(--ink-dark);
  }
  .card--front .practice-name__dot { background: var(--brand-blue); }
  .card--back .practice-name { font-size: 30px; color: var(--mark-silver); }
  .card--back .practice-name__dot { background: var(--mark-silver); width: 22px; height: 22px; }

  .holder { position: absolute; left: 48px; top: 150px; }
  .holder__name {
    font-family: "Roboto Condensed", sans-serif; font-weight: 700;
    font-size: 29px; color: var(--ink-dark); text-transform: uppercase;
    letter-spacing: .3px;
  }
  .holder__role {
    margin-top: 4px;
    font-family: "Open Sans", sans-serif; font-size: 17px; color: var(--brand-blue);
  }
  .divider {
    position: absolute; left: 48px; right: 48px; top: 236px;
    height: 2px; background: var(--rule-grey);
  }
  .contact {
    position: absolute; left: 48px; top: 262px; list-style: none;
    font-family: "Open Sans", sans-serif; font-size: 16px; color: var(--ink-grey);
  }
  .contact li { display: flex; align-items: center; gap: 12px; height: 28px; }
  .contact svg { width: 15px; height: 15px; fill: var(--brand-blue); flex: none; }
  .contact .contact__web { color: var(--brand-blue); }
  .address {
    position: absolute; right: 48px; top: 268px; text-align: right;
    font-family: "Open Sans", sans-serif; font-size: 16px; line-height: 26px;
    color: var(--ink-grey); font-style: normal;
  }
</style>
</head>
<body>
<main class="canvas">
  <section class="card card--front" aria-label="Voorkant visitekaartje">
    <div class="practice-name"><span class="practice-name__dot"></span>Praktijk Vornhoute</div>
    <div class="holder">
      <h1 class="holder__name">Dr. Sanne Vornhoute-ter Kuilen</h1>
      <p class="holder__role">Psychiater/Kinder- en Jeugdpsychiater</p>
    </div>
    <div class="divider"></div>
    <ul class="contact">
      <li>
        <svg viewBox="0 0 16 16" aria-hidden="true"><path d="M3.6 1.2l2.2 2.6c.3.4.3.9 0 1.3L4.7 6.4c.9 2 2.6 3.8 4.9 4.9l1.3-1.1c.4-.3.9-.3 1.3 0l2.6 2.2c.4.3.4.9.1 1.3l-1.2 1.3C12.3 16.4 1.2 8.4 2.3 1.3z"/></svg>
        06-51928764
      </li>
      <li>
        <svg viewBox="0 0 16 16" aria-hidden="true"><path d="M1 3h14v1.2L8 9 1 4.2zM1 5.8l7 4.8 7-4.8V13H1z"/></svg>
        info@praktijkvornhoute.nl
      </li>
      <li>
        <svg viewBox="0 0 16 16" aria-hidden="true"><path d="M8 1a7 7 0 100 14A7 7 0 008 1zm0 1.5c.8 0 1.7 1.6 2 4H6c.3-2.4 1.2-4 2-4zM2.6 6.5h2C4.5 7 4.5 7.5 4.5 8s0 1 .1 1.5h-2a5.5 5.5 0 010-3zm3.4 3h4c-.3 2.4-1.2 4-2 4s-1.7-1.6-2-4zm5.4 0c.1-.5.1-1 .1-1.5s0-1-.1-1.5h2a5.5 5.5 0 010 3z"/></svg>
        <span class="contact__web">www.praktijkvornhoute.nl</span>
      </li>
    </ul>
    <address class="address">Wouter Heskampstraat 14<br>3071 PX Rotterdam</address>
  </section>

  <section class="card card--back" aria-label="Achterkant visitekaartje">
    <div class="practice-name"><span class="practice-name__dot"></span>Praktijk Vornhoute</div>
  </section>
</main>
</body>
</html>
```